KVT Calculator

We have a calculator already created however the design seems to be very boring and bland. The calculators goal is to show graphic designers, web development firms, pr agencies, marketing firms how much revenue they can potentially make by offering a managed social media solution to their clients.

We want a great designer to make the calculator appealing to our audience.

It is an amazing offer and opportunity however I do not believe the current design does it justice

you can view and play with calculator live at http://sandbox.plorvinix.com/qzta/

```html
<!DOCTYPE html>
<html lang="en">
<head>
<meta charset="utf-8">
<title>Revenue Calculator</title>
<link rel="stylesheet" href="https://fonts.googleapis.com/css2?family=Arimo:wght@400;700&display=swap">
<style>
:root{
  --sky:#1b8fdc;
  --frame:#f3f5f8;
  --frame-edge:#c9d0da;
  --panel-top:#1e4fd6;
  --panel-bottom:#0d2fae;
  --navy:#0a1c86;
  --navy-deep:#061a6e;
  --label-text:#8fe4ff;
  --tab-blue-top:#5aa3d8;
  --tab-blue-bottom:#285b96;
  --tab-red-top:#f04848;
  --tab-red-bottom:#b81e1e;
  --basic:#8fc8b4;
  --basic-line:#b9ddd0;
  --basic-btn:#3c7e6a;
  --pro:#1a98ff;
  --pro-line:#62b9ff;
  --ent:#22b6f4;
  --ent-line:#74d2fa;
  --btn-blue:#1c64b8;
  --profit-text:#12302a;
  --white:#ffffff;
}
*{box-sizing:border-box;margin:0;padding:0}
html,body{width:1200px;height:612px;overflow:hidden}
body{background:var(--sky);font-family:"Arimo",sans-serif;position:relative}
.frame{position:absolute;left:18px;top:14px;width:1162px;height:578px;background:var(--frame);border-radius:34px;border:2px solid var(--frame-edge)}
.panel{position:absolute;left:46px;top:56px;width:1104px;height:410px;border-radius:16px;background:linear-gradient(180deg,var(--panel-top),var(--panel-bottom));box-shadow:inset 0 0 0 2px #2c5fe0}
.tab{position:absolute;height:41px;border-radius:8px 8px 0 0;color:var(--white);font-size:22px;font-weight:700;display:flex;align-items:center;justify-content:center;border:1px solid #9cc4e8;border-bottom:none}
.tab-term{left:82px;top:59px;width:164px;background:linear-gradient(180deg,var(--tab-blue-top),var(--tab-blue-bottom))}
.tab-blue{background:linear-gradient(180deg,var(--tab-blue-top),var(--tab-blue-bottom))}
.tab-red{background:linear-gradient(180deg,var(--tab-red-top),var(--tab-red-bottom))}
.term-gauge{position:absolute;left:94px;top:100px;width:140px;height:351px}
.row-label{position:absolute;left:260px;width:291px;height:58px;background:var(--navy);border-radius:6px;color:var(--label-text);font-size:18px;font-weight:700;display:flex;align-items:center;padding-left:24px}
.plan{position:absolute;top:100px;width:157px;height:346px;border-radius:0 0 8px 8px;border:2px solid rgba(255,255,255,.55);border-top:none}
.plan-basic{left:581px;background:var(--basic);--line:var(--basic-line);--btn:var(--basic-btn)}
.plan-pro{left:763px;background:var(--pro);--line:var(--pro-line);--btn:var(--btn-blue)}
.plan-ent{left:945px;background:var(--ent);--line:var(--ent-line);--btn:var(--btn-blue)}
.cell{position:absolute;left:0;right:0;display:flex;align-items:center;justify-content:center;color:var(--white);font-size:19px;font-weight:700;border-bottom:1px solid var(--line)}
.cell-clients{top:0;height:84px}
.cell-pay{top:84px;height:94px}
.cell-price{top:178px;height:69px}
.cell-profit{top:247px;height:93px;border-bottom:none;color:var(--profit-text);font-size:21px}
.stepper{display:flex;align-items:center;justify-content:space-between;width:100%;padding:0 6px}
.btn{width:28px;height:25px;background:var(--btn);border:1px solid var(--white);border-radius:3px;color:var(--white);font-size:20px;line-height:22px;text-align:center;font-weight:700}
.total{position:absolute;left:111px;top:480px;width:977px;height:77px;background:var(--navy-deep);border-radius:10px 10px 24px 24px;color:var(--white);font-size:40px;display:flex;align-items:center;justify-content:center}
.screw{position:absolute;width:10px;height:10px;border-radius:50%;background:radial-gradient(circle,#9aa3ad,#5d6670)}
</style>
</head>
<body>
<div class="frame"></div>
<section class="panel"></section>

<div class="tab tab-term">TERM (YRS)</div>
<svg class="term-gauge" viewBox="0 0 140 351" aria-hidden="true">
  <path d="M0 0 H140 V281 A70 70 0 0 1 0 281 Z" fill="#0a1c86"/>
  <rect x="66" y="10" width="9" height="262" fill="#fff"/>
  <rect x="66" y="272" width="9" height="45" fill="#111"/>
  <g stroke="#fff" stroke-width="3">
    <line x1="30" y1="30" x2="88" y2="30"/><line x1="30" y1="63" x2="88" y2="63"/>
    <line x1="30" y1="95" x2="88" y2="95"/><line x1="30" y1="128" x2="88" y2="128"/>
    <line x1="30" y1="161" x2="88" y2="161"/><line x1="30" y1="194" x2="88" y2="194"/>
    <line x1="30" y1="227" x2="88" y2="227"/><line x1="30" y1="260" x2="88" y2="260"/>
    <line x1="30" y1="293" x2="88" y2="293"/>
  </g>
  <circle cx="70" cy="276" r="16" fill="#e0242a" stroke="#fff" stroke-width="2"/>
  <path d="M62 281 L70 272 L78 281" fill="none" stroke="#fff" stroke-width="3.5"/>
</svg>

<div class="row-label" style="top:120px">Clint per month:</div>
<div class="row-label" style="top:196px">You pay:</div>
<div class="row-label" style="top:271px">Your client pays:</div>
<div class="row-label" style="top:346px">Monthly profit (Year 2):</div>

<div class="tab tab-blue" style="left:568px;top:59px;width:179px">BASIC</div>
<div class="tab tab-red" style="left:751px;top:59px;width:179px">PRO</div>
<div class="tab tab-blue" style="left:935px;top:59px;width:181px">ENTERPRISE</div>

<div class="plan plan-basic">
  <div class="cell cell-clients"><div class="stepper"><span class="btn">−</span>1<span class="btn">+</span></div></div>
  <div class="cell cell-pay">$197</div>
  <div class="cell cell-price"><div class="stepper"><span class="btn">−</span>$297<span class="btn">+</span></div></div>
  <div class="cell cell-profit">$2,400</div>
</div>
<div class="plan plan-pro">
  <div class="cell cell-clients"><div class="stepper"><span class="btn">−</span>1<span class="btn">+</span></div></div>
  <div class="cell cell-pay">$297</div>
  <div class="cell cell-price"><div class="stepper"><span class="btn">−</span>$497<span class="btn">+</span></div></div>
  <div class="cell cell-profit">$4,800</div>
</div>
<div class="plan plan-ent">
  <div class="cell cell-clients"><div class="stepper"><span class="btn">−</span>1<span class="btn">+</span></div></div>
  <div class="cell cell-pay">$2500</div>
  <div class="cell cell-price"><div class="stepper"><span class="btn">−</span>$4000<span class="btn">+</span></div></div>
  <div class="cell cell-profit">$36,000</div>
</div>

<div class="total">Monthly profit by the end of year 2: $43,200</div>
<span class="screw" style="left:71px;top:543px"></span>
<span class="screw" style="left:1114px;top:543px"></span>
</body>
</html>
```